Brin E's Jar Lable for kids Christmas gifts

Looking to get a wrap around label made for a quart canning jar. I would like it to have my kids head on it also. I was thinking in a silhouette form on both ends of the wrap( added a quick sketch up). We will be canning Pickles and giving them away as gifts this year. Also might be selling a few at a frames market. The brand name is " Brin E's" ( at the moment) So if you could think of a cool logo around that would be awesome also. I am an Orange and Black fan but I am up for suggestions also. Do you think this might be something you could help me with?

The second attached graphic is what I would like my kids faces to look similer to. Art wise. The sketch is of what the ends of the labels need to look like. Not a full face but a half of each of there faces on both ends of the lable.

Colors
f78f20
000000
757575

Requirements
Nice to have
• antique lable feel

```html
<!DOCTYPE html>
<html lang="en">
<head>
<meta charset="utf-8">
<title>Brin E's Jar Label</title>
<link rel="stylesheet" href="https://fonts.googleapis.com/css2?family=Arimo:wght@400&display=swap">
<style>
  :root {
    --backdrop: #4a4a4a;
    --label-black: #000000;
    --ink-white: #ffffff;
    --portrait-tone-light: #3a3a3a;
    --portrait-tone-dark: #141414;
  }
  html, body {
    margin: 0;
    padding: 0;
    width: 1200px;
    height: 960px;
    overflow: hidden;
    background: var(--backdrop);
    font-family: "Arimo", Arial, sans-serif;
  }
  .jar-label {
    position: absolute;
    left: 20px;
    top: 128px;
    width: 1160px;
    height: 703px;
    background: var(--label-black);
    color: var(--ink-white);
  }
  .portrait-halves {
    position: absolute;
    left: 15px;
    top: 174px;
    width: 331px;
    height: 351px;
    border-radius: 46% 46% 40% 40%;
    background: radial-gradient(ellipse at 50% 35%, var(--portrait-tone-light), var(--portrait-tone-dark) 75%);
  }
  .side-description {
    position: absolute;
    left: 436px;
    top: 71px;
    width: 560px;
    height: 130px;
    transform-origin: 0 0;
    transform: translateY(560px) rotate(-90deg);
    margin: 0;
    font-size: 19px;
    line-height: 26px;
    text-align: center;
  }
  .brand-name {
    position: absolute;
    left: 720px;
    top: 50px;
    margin: 0;
    font-size: 116px;
    font-weight: 400;
    line-height: 1;
    white-space: nowrap;
  }
  .front-description {
    position: absolute;
    left: 722px;
    top: 272px;
    width: 222px;
    margin: 0;
    font-size: 19px;
    line-height: 24.4px;
  }
</style>
</head>
<body>
  <main class="jar-label">
    <div class="portrait-halves" role="img" aria-label="White line-art silhouette halves of two children's faces, one on each end of the label"></div>
    <p class="side-description">A pickled cucumber is a cucumber that has been pickled in a brine, vinegar, or other solution and left to ferment for a period of time, by either immersing the cucumbers in an acidic solution or through souring by lacto-fermentation</p>
    <h1 class="brand-name">Brin E's</h1>
    <p class="front-description">A pickled cucumber is a cucumber that has been pickled in a brine, vinegar, or other solution and left to ferment for a period of time, by either immersing the cucumbers in an acidic solution or through souring by lacto-fermentation</p>
  </main>
</body>
</html>
```